In Home Senior Care Agency Business Card Design Needed

At Silver Birch Helpers, we don't just work in the care-giving industry. We truly care.

We are dedicated to providing personable, hands-on and integrated caring services that aim to help people maintain safe and comfortable life standards within the familiar settings of their own homes.

We would like to see designs that use my logo colors obviously. The final design will be modern, yet professional and semi-minimalistic. It should communicate an well-established company that is innovative. We would also like the design to have that 'flat' design look. Ideally having the design roll over to the backend of the card. Most likely it will be printed on a Matte paper with a die cut (either 2 rounded corners -leaf cut) or all rounded.

Target Market(s)

Baby boomer generation. 45 years and older.

Industry/Entity Type

Business

Contact Information for Business Card

Text for Front:
Slogan somewhere "Helping Hands. Close To Home.”

Darren Whitlow
President

Cell: 917.284.6051
Phone: 917.512.7368
E: Darren@silverbirchhelpers.com
W: www.SilverBirchHelpers.com

Back:
-Meal Preparation
-Transportation
-Light Housekeeping
-Bathing Assistance
-Companionship

Font styles to use
Serif
Sans Serif

Requirements
Must have
• Flat, modern, professional design. Not too many colors. Match my colors in logo. Design of card must reflect from the front onto the back. Evenly spaced font.
Nice to have
• Try to work off current logo scheme, but logo may need to be redesigned.
Should not have
• Not too many colors.

```html
<!DOCTYPE html>
<html lang="en">
<head>
<meta charset="utf-8">
<title>Silver Birch Helpers – Business Card</title>
<link rel="stylesheet" href="https://fonts.googleapis.com/css2?family=Libre+Baskerville&family=Poppins:wght@400;600&display=swap">
<style>
  :root {
    --canvas: #ebeeef;
    --card: #ffffff;
    --green: #07693a;
    --gold: #f6b142;
    --ink: #333333;
    --ink-soft: #444444;
  }
  html, body { margin: 0; padding: 0; overflow: hidden; }
  body {
    width: 1018px; height: 1200px;
    background: var(--canvas);
    position: relative;
    font-family: "Poppins", Arial, sans-serif;
  }
  .card {
    position: absolute;
    left: 105px;
    width: 787px; height: 467px;
    background: var(--card);
    overflow: hidden;
  }
  .card svg.waves { position: absolute; inset: 0; }
  .card-front { top: 110px; border-radius: 120px 8px 120px 0; }
  .card-back  { top: 624px; border-radius: 0 120px 0 120px; }

  .brand-name {
    position: absolute; left: 0; right: 0; top: 160px;
    text-align: center;
    font-family: "Libre Baskerville", Georgia, serif;
    font-size: 56px; line-height: 1.1;
    color: var(--green);
    margin: 0; font-weight: 400;
  }
  .services {
    position: absolute; left: 0; right: 0; top: 370px;
    margin: 0; padding: 0; list-style: none;
    text-align: center;
    color: #fff; font-weight: 600; font-size: 24px; line-height: 40px;
  }
  .services .dot {
    display: inline-block; width: 13px; height: 13px; border-radius: 50%;
    background: var(--gold); margin: 0 6px 3px; vertical-align: middle;
  }

  .contact { position: absolute; left: 97px; top: 90px; color: var(--ink-soft); }
  .contact .name { font-weight: 600; font-size: 22px; color: var(--ink); margin: 0; }
  .contact .role { font-size: 22px; margin: 4px 0 20px; }
  .contact ul { list-style: none; margin: 0; padding: 0; font-size: 22px; line-height: 34px; }
  .contact li { display: flex; align-items: center; gap: 5px; }
  .contact svg { width: 20px; height: 20px; flex: none; }
  .slogan {
    position: absolute; left: 0; right: 0; top: 392px;
    text-align: center; margin: 0;
    color: var(--gold); font-weight: 600; font-size: 26px;
  }
</style>
</head>
<body>

<section class="card card-front">
  <svg class="waves" viewBox="0 0 787 467" aria-hidden="true">
    <path d="M0 340 L560 340 C680 340 770 300 787 222 L787 467 L0 467 Z" fill="var(--gold)"/>
    <path d="M0 348 L560 348 C690 348 776 306 787 236 L787 467 L0 467 Z" fill="var(--green)"/>
  </svg>
  <h1 class="brand-name">Silver Birch<br>Helpers</h1>
  <ul class="services">
    <li>Meal Preparation<span class="dot"></span>Transportation<span class="dot"></span>Companionship</li>
    <li>Light Housekeeping<span class="dot"></span>Bathing Assistance</li>
  </ul>
</section>

<section class="card card-back">
  <svg class="waves" viewBox="0 0 787 467" aria-hidden="true">
    <path d="M0 240 C10 320 60 358 150 358 L787 358 L787 467 L0 467 Z" fill="var(--gold)"/>
    <path d="M0 256 C12 330 66 366 150 366 L787 366 L787 467 L0 467 Z" fill="var(--green)"/>
  </svg>
  <div class="contact">
    <p class="name">Darren Whitlow</p>
    <p class="role">President</p>
    <ul>
      <li><svg viewBox="0 0 20 20" aria-label="Cell"><rect x="4" y="2" width="12" height="16" rx="2" fill="none" stroke="var(--green)" stroke-width="1.6"/><line x1="8" y1="15" x2="12" y2="15" stroke="var(--green)" stroke-width="1.4"/></svg>917.284.6051</li>
      <li><svg viewBox="0 0 20 20" aria-label="Phone"><path d="M5 2 L8 2 L9 6 L7 8 C8 11 9 12 12 13 L14 11 L18 12 L18 15 C18 17 16 18 14 18 C8 17 3 12 2 6 C2 4 3 2 5 2 Z" fill="var(--green)"/></svg>917.512.7368</li>
      <li><svg viewBox="0 0 20 20" aria-label="Email"><rect x="2" y="4" width="16" height="12" fill="none" stroke="var(--green)" stroke-width="1.6"/><path d="M2 4 L10 11 L18 4" fill="none" stroke="var(--green)" stroke-width="1.6"/></svg>Darren@silverbirchhelpers.com</li>
      <li><svg viewBox="0 0 20 20" aria-label="Website"><circle cx="10" cy="10" r="8" fill="none" stroke="var(--green)" stroke-width="1.6"/><ellipse cx="10" cy="10" rx="3.5" ry="8" fill="none" stroke="var(--green)" stroke-width="1.3"/><line x1="2" y1="10" x2="18" y2="10" stroke="var(--green)" stroke-width="1.3"/></svg>www.SilverBirchHelpers.com</li>
    </ul>
  </div>
  <p class="slogan">“Helping Hands. Close To Home.”</p>
</section>

</body>
</html>
```